Cedar Grove Worship Chapel CG- Theme for 2022

We, Cedar Grove Worship Chapel of Willow Bend, need a design for a 4' x 6' banner that will be placed on two walls in the main sanctuary. The banner is to communicate/advertise the church's theme for 2022, "He Will Make All Things New: A New You - 2022" Revelations 21:5. The design should include our logo and church name. Use the color purple. We have not worshipped in our church building since 2020 due to the COVID pandemic. This banner should be reflective of change, newness as we plan to re-enter the building this spring. Our congregation demographic is 95% African American, 5% Hispanic. Our home base is Tampa, Florida (USA), but we have a large social media following, primarily due to the pandemic.

Target Market(s)

Church members, Ages 1-99; male and female

Industry/Entity Type

Religious

Font styles to use
Serif

Colors
0094D4
00A9DD
6FCCEA
C7EBF8
E9F6FB
00AB8E
00BBA5
67D7C9
C6EFE9
E9F9F6
6B429C
8869AF
B7A5CE
E3DAEB
F3F0F8

Requirements
Must have
• Theme, scripture, church logo and color purple

```html
<!DOCTYPE html>
<html lang="en">
<head>
<meta charset="utf-8">
<title>He Will Make All Things New – A New You 2022</title>
<link href="https://fonts.googleapis.com/css2?family=Poppins:wght@600;700&family=Bebas+Neue&family=Montserrat:wght@500;700&family=Tinos:wght@700&display=swap" rel="stylesheet">
<style>
  :root {
    --purple-deep: #4a0f8f;
    --purple-main: #6a1fb4;
    --purple-soft: #8f4fd0;
    --purple-band: rgba(150, 90, 220, 0.55);
    --purple-line: #9a5ee0;
    --white: #ffffff;
    --badge-dark: #111018;
    --gold-light: #fbe6a6;
    --gold-mid: #c99a4a;
    --gold-deep: #5e3f1c;
  }
  * { margin: 0; padding: 0; box-sizing: border-box; }
  html, body { width: 1200px; height: 675px; overflow: hidden; background: var(--purple-deep); }
  .banner {
    position: relative;
    width: 1200px;
    height: 675px;
    overflow: hidden;
    background:
      radial-gradient(ellipse 420px 300px at 330px 250px, rgba(190,140,240,0.35), transparent 70%),
      radial-gradient(ellipse 500px 260px at 900px 80px, rgba(170,110,230,0.45), transparent 70%),
      radial-gradient(ellipse 300px 200px at 100px 40px, rgba(160,100,220,0.35), transparent 70%),
      linear-gradient(160deg, var(--purple-main) 0%, var(--purple-deep) 55%, var(--purple-main) 100%);
    color: var(--white);
  }
  .theme-title {
    position: absolute;
    left: 40px;
    top: 75px;
    width: 600px;
    text-align: center;
    font-family: "Poppins", sans-serif;
    font-weight: 700;
    font-size: 77px;
    line-height: 82px;
    white-space: nowrap;
    text-shadow: 0 3px 10px rgba(40, 0, 80, 0.4);
  }
  .theme-title .line { display: block; }
  .theme-subtitle {
    position: absolute;
    left: 50px;
    top: 355px;
    width: 570px;
    text-align: center;
    white-space: nowrap;
    font-family: "Bebas Neue", sans-serif;
    font-size: 100px;
    line-height: 100px;
    letter-spacing: 1px;
    color: var(--white);
    -webkit-text-stroke: 2px var(--purple-deep);
    text-shadow: 3px 4px 0 var(--purple-deep), 5px 6px 0 var(--white);
  }
  .scripture {
    position: absolute;
    left: 482px;
    top: 452px;
    font-family: "Tinos", serif;
    font-weight: 700;
    font-size: 17px;
    white-space: nowrap;
  }
  .info-band {
    position: absolute;
    left: 0;
    top: 532px;
    width: 1200px;
    height: 64px;
    background: linear-gradient(90deg, var(--purple-band), rgba(150,90,220,0.35));
    border-top: 1px solid var(--purple-line);
    border-bottom: 1px solid var(--purple-line);
  }
  .church-name {
    position: absolute;
    left: 72px;
    top: 540px;
    font-family: "Montserrat", sans-serif;
    font-weight: 700;
    font-size: 18px;
    white-space: nowrap;
  }
  .church-address {
    position: absolute;
    left: 136px;
    top: 567px;
    font-family: "Montserrat", sans-serif;
    font-weight: 500;
    font-size: 16.5px;
    letter-spacing: 0.5px;
    white-space: nowrap;
  }
  .web-row {
    position: absolute;
    left: 235px;
    top: 610px;
    display: flex;
    align-items: center;
    gap: 14px;
    font-family: "Montserrat", sans-serif;
    font-weight: 700;
    font-size: 16px;
    white-space: nowrap;
  }
  .social-dot {
    width: 24px;
    height: 24px;
    border-radius: 50%;
    background: var(--white);
  }
  .web-address { margin-right: 8px; }
  .scene-photo {
    position: absolute;
    left: 640px;
    top: 238px;
    width: 560px;
    height: 437px;
  }
  .church-mark {
    position: absolute;
    left: 756px;
    top: 25px;
    width: 230px;
    height: 230px;
    border-radius: 50%;
    background: var(--badge-dark);
    border: 5px solid var(--purple-main);
    box-shadow: 0 0 28px 10px rgba(230, 200, 255, 0.7);
    display: flex;
    align-items: center;
    justify-content: center;
    text-align: center;
    padding: 30px;
    font-family: "Montserrat", sans-serif;
    font-weight: 700;
    font-size: 21px;
    line-height: 30px;
    color: var(--white);
  }
</style>
</head>
<body>
  <main class="banner">
    <svg class="scene-photo" viewBox="0 0 560 437" role="img" aria-label="Sunlit autumn forest path with a person walking toward the light">
      <defs>
        <radialGradient id="forestLight" cx="0.6" cy="0.25" r="0.8">
          <stop offset="0" stop-color="#fbe6a6"/>
          <stop offset="0.45" stop-color="#c99a4a"/>
          <stop offset="1" stop-color="#5e3f1c"/>
        </radialGradient>
      </defs>
      <path d="M60 40 L140 22 L230 30 L330 10 L420 28 L500 60 L520 110 L510 170 L530 240 L520 300 L545 360 L540 437 L70 437 L40 400 L20 340 L35 280 L10 220 L25 160 L15 100 Z" fill="url(#forestLight)"/>
    </svg>

    <h1 class="theme-title">
      <span class="line">He Will</span>
      <span class="line">Make All</span>
      <span class="line">Things New</span>
    </h1>
    <p class="theme-subtitle">A New You - 2022</p>
    <p class="scripture">Revelations 21:5</p>

    <div class="church-mark">Cedar Grove Worship Chapel CG</div>

    <div class="info-band"></div>
    <p class="church-name">Cedar Grove Worship Chapel of Willow Bend</p>
    <p class="church-address">4120 Linden Row Willow Bend, FL 33900</p>

    <div class="web-row">
      <span class="web-address">www.cedargrovecg.org</span>
      <span class="social-dot"></span>
      <span class="social-dot"></span>
    </div>
  </main>
</body>
</html>
```